Up to the Challenge? Canadian based consulting company needs a two sided business card design

A Canadian based security risk management consulting company needs a two-sided business card design. What we do is provide advice and guidance related to emergency, security and business continuity management for small, medium and large companies to help ensure the protection of their people, assets, information, services, operations and reputation.

The final design should be simple, only one or two colours, eye catching, professional and one that makes people look at three or more times just because it looks so darn good.

I have include examples of business cards I like.

Target Market(s)

Small, medium and large companies.

Industry/Entity Type

Security

Contact Information for Business Card

Business Card Size: Standard size of 3.5" (89mm) x 2.0" (51mm) - (see full specifications and guides on PRINTA's website if required)
Card Stock: Looking to use PRINTA's Velda 32pt stock textured paper - seam colour either chili red or black
Business Name: The Harrowfield Group
Website: www.theharrowfieldgroup.example
Telephone: (555)214-0397
Name: Dana Forsythe
Position: Principle
e-mail: Dana.Forsythe@theharrowfieldgroup.example

Font styles to use
Serif

Colors
ec1f27
000000
9d9d9d
aaaaaa
606060

Requirements
Must have
• - "The Harrowfield Group" logo (see uploaded files). I have included grey scale and colour versions.
• - Business card details (as above)
Nice to have
• - One side black or grey scale.
• - Other side would likely be white.
• - Everyone likes the silver logo on the black background.
• - Small element of colour i.e. red but I'm leaning more to greyscale.
Should not have
• - A lot of colour. Keep it simple.

```html
<!DOCTYPE html>
<html lang="en">
<head>
<meta charset="utf-8">
<title>The Harrowfield Group – Business Card</title>
<link href="https://fonts.googleapis.com/css2?family=Cinzel:wght@400&family=PT+Serif:ital,wght@0,400;0,700;1,400&display=swap" rel="stylesheet">
<style>
  :root {
    --backdrop: #3a3a3a;
    --card-black: #000000;
    --card-white: #ffffff;
    --silver: #9d9d9d;
    --ink: #1e1e1e;
    --icon: #2a2a2a;
  }
  html, body {
    margin: 0;
    padding: 0;
    width: 1200px;
    height: 1200px;
    overflow: hidden;
    background: var(--backdrop);
  }
  .canvas {
    position: relative;
    width: 1200px;
    height: 1200px;
  }
  .card {
    position: absolute;
    left: 217px;
    width: 767px;
    height: 425px;
    box-sizing: border-box;
  }
  .card--front {
    top: 157px;
    background: var(--card-black);
  }
  .card--back {
    top: 616px;
    background: var(--card-white);
    border: 2px solid #cfcfcf;
  }
  .wordmark {
    position: absolute;
    left: 0;
    right: 0;
    text-align: center;
    font-family: "Cinzel", serif;
    font-weight: 400;
    color: var(--silver);
    line-height: 1;
    margin: 0;
  }
  .wordmark__main {
    top: 200px;
    font-size: 40px;
    letter-spacing: 1px;
  }
  .wordmark__sub {
    top: 254px;
    font-size: 30px;
    letter-spacing: 4px;
  }
  .person {
    position: absolute;
    left: 99px;
    top: 145px;
    font-family: "PT Serif", serif;
    color: var(--ink);
  }
  .person__name {
    margin: 0;
    font-size: 40px;
    font-weight: 700;
    line-height: 44px;
  }
  .person__role {
    margin: 0;
    font-size: 26px;
    font-style: italic;
    line-height: 30px;
  }
  .contacts {
    position: absolute;
    left: 70px;
    top: 258px;
    margin: 0;
    padding: 0;
    list-style: none;
    font-family: "PT Serif", serif;
    font-size: 20px;
    color: var(--ink);
  }
  .contacts__item {
    display: flex;
    align-items: center;
    height: 26.5px;
  }
  .contacts__icon {
    width: 20px;
    height: 20px;
    margin-right: 9px;
    flex: none;
  }
</style>
</head>
<body>
<main class="canvas">
  <section class="card card--front" aria-label="Card front">
    <p class="wordmark wordmark__main">THE HARROWFIELD</p>
    <p class="wordmark wordmark__sub">GROUP</p>
  </section>

  <section class="card card--back" aria-label="Card back">
    <div class="person">
      <h1 class="person__name">Dana Forsythe</h1>
      <p class="person__role">Principle</p>
    </div>
    <ul class="contacts">
      <li class="contacts__item">
        <svg class="contacts__icon" viewBox="0 0 20 20" aria-hidden="true">
          <circle cx="10" cy="10" r="10" fill="var(--icon)"/>
          <path d="M5 9 Q10 4 15 9 L13.5 10 L12.5 8.5 Q10 7.5 7.5 8.5 L6.5 10 Z" fill="#fff"/>
          <rect x="6.5" y="10.5" width="7" height="4" rx="1" fill="#fff"/>
        </svg>
        <span>Telephone: (555)214-0397</span>
      </li>
      <li class="contacts__item">
        <svg class="contacts__icon" viewBox="0 0 20 20" aria-hidden="true">
          <circle cx="10" cy="10" r="10" fill="var(--icon)"/>
          <rect x="5" y="6.5" width="10" height="7" fill="none" stroke="#fff" stroke-width="1.3"/>
          <path d="M5 6.5 L10 11 L15 6.5" fill="none" stroke="#fff" stroke-width="1.3"/>
        </svg>
        <span>e-mail: Dana.Forsythe@theharrowfieldgroup.example</span>
      </li>
      <li class="contacts__item">
        <svg class="contacts__icon" viewBox="0 0 20 20" aria-hidden="true">
          <circle cx="10" cy="10" r="10" fill="var(--icon)"/>
        </svg>
        <span>Netlink/ca.netlink.example/in/danaforsythe</span>
      </li>
      <li class="contacts__item">
        <svg class="contacts__icon" viewBox="0 0 20 20" aria-hidden="true">
          <circle cx="10" cy="10" r="10" fill="var(--icon)"/>
          <circle cx="10" cy="10" r="6" fill="none" stroke="#fff" stroke-width="1.1"/>
          <ellipse cx="10" cy="10" rx="2.6" ry="6" fill="none" stroke="#fff" stroke-width="1.1"/>
          <line x1="4" y1="10" x2="16" y2="10" stroke="#fff" stroke-width="1.1"/>
        </svg>
        <span>www.theharrowfieldgroup.example</span>
      </li>
    </ul>
  </section>
</main>
</body>
</html>
```